依頼詳細
・表面のみの名刺 (裏面は白紙)
・横型、縦型はお問い致しません
・tel、e-mailなどはアイコン+文字でお願いします
・Facebookは画像でお願いします
・自然的で、シンプル的なものをお願いします
・こちらからご提出する画像は3点となりますが、画像が荒いので綺麗に加工をお願い致します
記載項目
詳しくは添付のワードファイルをご参照ください

表面:会社名/キャッチフレーズ/役職/氏名/氏名の英語表記/〒/住所/Tel/E-mail/HP/Facebook
※ イラストレーター形式 (.ai)を頂いたら編集させてもらう予定なので、会社名等は、○○等で結構です。
裏面:ございません。

キャッチフレーズ: 「楢の森のきれいな清流で実った岩之介大根誕生の里」
※ もっと良い、キャッチフレーズがありましたらお願いします
希望イメージ
シンプル 複雑
単色 カラフル
暗い 明るい
日常 高級
遊び心 厳粛
未来的 伝統的
女性的 男性的
希望する色
赤、青、緑
納品ファイル
• 高解像度JPG (.jpg)
• イラストレーター形式 (.ai)
補足説明
可能であれば、イラストレーターCS2で編集できる形式で、お願い致します。。
依頼公開後の追記内容
申し訳ありません。

気だてのいい大根なんです。楢沢岩ノ俣の畑でかわいがられて育ちました。」
の文章を入れていただけませんでしょうか。

既に、アップロードしております画像に書いてある文字です。

以上、お願い致します。
■ 選んだ理由

会社のイメージに、ピッタリ合っていました。

■ 提案者全員のお礼・コメント

提案を頂きました、ランサー方々へ

素晴らしいデザインをありがとございました。
また、機会がございましたら宜しくお願いします。

```html
<!DOCTYPE html>
<html lang="ja">
<head>
<meta charset="utf-8">
<title>岩之介大根 名刺</title>
<link rel="stylesheet" href="https://fonts.googleapis.com/css2?family=M+PLUS+Rounded+1c:wght@400;500;700&family=Noto+Sans+JP:wght@400;500&family=Noto+Serif+JP:wght@500&display=swap">
<style>
  :root {
    --ink: #1a1a1a;
    --crimson: #8c1433;
    --rose: #c97a8c;
    --paper: #ffffff;
    --icon-blue: #3d6fb0;
  }
  html, body {
    margin: 0;
    padding: 0;
    width: 726px;
    height: 1200px;
    overflow: hidden;
    background: var(--paper);
  }
  .card {
    position: relative;
    width: 726px;
    height: 1200px;
    overflow: hidden;
    background: linear-gradient(200deg, #ffffff 8%, #f6e6ea 42%, #dba3b0 78%, #c97a8c 100%);
    font-family: "Noto Sans JP", sans-serif;
    color: var(--ink);
  }
  .header {
    position: absolute;
    left: 0; top: 0;
    width: 726px; height: 145px;
    background: var(--paper);
    border-bottom: 3px solid var(--rose);
  }
  .mascot-mini {
    position: absolute;
    left: 48px; top: 14px;
    width: 50px; height: 100px;
    border-radius: 25px 25px 22px 22px;
    background: linear-gradient(180deg, #9bbf6a 0%, #f4f1e8 30%, #ece7db 100%);
  }
  .catchphrase {
    position: absolute;
    right: 28px; top: 14px;
    margin: 0;
    font-family: "M PLUS Rounded 1c", sans-serif;
    text-align: right;
    color: var(--ink);
  }
  .catchphrase .line1 { display: block; font-size: 32px; letter-spacing: 2px; line-height: 1.5; font-weight: 400; }
  .catchphrase .line2 { display: block; font-size: 38px; letter-spacing: 6px; line-height: 1.5; font-weight: 500; }

  .brand-lettering {
    position: absolute;
    left: 36px; top: 178px;
    width: 206px; height: 342px;
    border-radius: 30px;
    background: linear-gradient(170deg, #a51d40 0%, #8c1433 100%);
    opacity: 0.9;
  }
  .company {
    position: absolute;
    left: 288px; top: 218px;
    color: var(--ink);
  }
  .company .sub { display: block; font-size: 36px; line-height: 1.3; }
  .company .main { display: block; font-size: 56px; line-height: 1.25; font-weight: 500; }

  .title {
    position: absolute;
    left: 290px; top: 372px;
    font-size: 28px;
    letter-spacing: 1px;
  }
  .name {
    position: absolute;
    left: 290px; top: 450px;
    font-size: 38px;
    letter-spacing: 3px;
    line-height: 1.2;
  }
  .name-en {
    position: absolute;
    left: 290px; top: 500px;
    font-size: 32px;
    letter-spacing: 1px;
    font-family: "M PLUS Rounded 1c", sans-serif;
  }
  .message {
    position: absolute;
    right: 552px; top: 570px;
    height: 260px;
    margin: 0;
    writing-mode: vertical-rl;
    font-family: "Noto Serif JP", serif;
    font-weight: 500;
    font-size: 28px;
    line-height: 1.2;
    letter-spacing: 1px;
    color: var(--crimson);
  }
  .message .place { font-size: 24px; }
  .mascot {
    position: absolute;
    left: 496px; top: 750px;
    width: 132px; height: 132px;
    border-radius: 50%;
    background: radial-gradient(circle at 45% 40%, #ffffff 0%, #f2c9d1 55%, #c95a74 100%);
  }

  .contacts {
    position: absolute;
    left: 48px; top: 912px;
    margin: 0; padding: 0;
    list-style: none;
    font-size: 28px;
    letter-spacing: 1px;
  }
  .contacts li {
    display: flex;
    align-items: center;
    height: 37px;
  }
  .contacts .long { font-size: 26px; letter-spacing: 0; }
  .contacts .icon {
    width: 36px; height: 30px;
    margin-right: 22px;
    flex: none;
  }
  .contacts .square {
    width: 28px; height: 28px;
    margin: 0 26px 0 4px;
    background: var(--icon-blue);
    border-radius: 4px;
    flex: none;
  }
</style>
</head>
<body>
<main class="card">
  <header class="header">
    <div class="mascot-mini" role="img" aria-label="大根のキャラクターの小さなイラスト"></div>
    <p class="catchphrase">
      <span class="line1">楢の森のきれいな清流で実った</span>
      <span class="line2">岩之介大根誕生の里</span>
    </p>
  </header>

  <div class="brand-lettering" role="img" aria-label="筆文字のロゴ「岩之介」"></div>

  <div class="company">
    <span class="sub">□□□□□□□</span>
    <span class="main">□□□□□□□</span>
  </div>
  <div class="title">代表取締役</div>
  <div class="name">山田太郎</div>
  <div class="name-en">YAMADA,taro</div>

  <p class="message">気だてのいい<br>大根なんです。<br><span class="place">楢沢岩ノ俣の畑で</span><br>かわいがられて<br>育ちました。</p>
  <div class="mascot" role="img" aria-label="大根のキャラクターのイラスト"></div>

  <ul class="contacts">
    <li>
      <svg class="icon" viewBox="0 0 36 32" aria-hidden="true"><rect x="1" y="4" width="34" height="24" rx="12" fill="none" stroke="#555" stroke-width="2.5"/><path d="M11 11h14M11 16h14M18 16v9" stroke="#555" stroke-width="2.5"/></svg>
      <span>123-4567</span>
    </li>
    <li>
      <span class="icon" aria-hidden="true"></span>
      <span class="long">□□□□□□□□□□□□□□□□□□□□</span>
    </li>
    <li>
      <svg class="icon" viewBox="0 0 36 32" aria-hidden="true"><circle cx="18" cy="16" r="15" fill="#333"/><path d="M12 9c2-1 3 0 4 3l-2 2c1 3 3 5 6 6l2-2c3 1 4 2 3 4-1 2-4 3-7 1-4-2-7-5-8-9-1-3 0-4 2-5z" fill="#fff"/></svg>
      <span>□□-□□□-□□□□</span>
    </li>
    <li>
      <svg class="icon" viewBox="0 0 36 32" aria-hidden="true"><rect x="2" y="6" width="32" height="21" rx="2" fill="#fff" stroke="#333" stroke-width="2.5"/><path d="M3 8l15 11L33 8" fill="none" stroke="#333" stroke-width="2.5"/></svg>
      <span>□□□@□□□□□□</span>
    </li>
    <li>
      <span class="square" aria-hidden="true"></span>
      <span>HP/http://www/□□□□□□</span>
    </li>
    <li>
      <span class="square" aria-hidden="true"></span>
      <span class="long">□□□□□□□□□□□□□□□□□□□□</span>
    </li>
  </ul>
</main>
</body>
</html>
```